Plastic Business Cards

I am looking for a plastic business card that matches the theme of my company.

Attached will be logo and template to Prindlecraft for printing.

On card please include the following information:

Logo
612-437-9158 Call or Text
www.GlintvaleCo.com

Window Cleaning
Gutter Cleaning & Covers
Christmas Lighting

200+ 5 Star Reviews

```html
<!DOCTYPE html>
<html lang="en">
<head>
<meta charset="utf-8">
<title>Glintvale Window Cleaning – Plastic Business Cards</title>
<link href="https://fonts.googleapis.com/css2?family=Montserrat:wght@800&display=swap" rel="stylesheet">
<style>
  :root{
    --stage:#e5e5e3;
    --sky-deep:#1592d6;
    --sky-mid:#3fb6ea;
    --sky-light:#bfe6f8;
    --white:#ffffff;
    --lime-deep:#9cc43a;
    --lime-bright:#c6d92c;
    --navy:#16305f;
    --text-blue:#2ea6e6;
  }
  *{margin:0;padding:0;box-sizing:border-box}
  html,body{width:1200px;height:846px;overflow:hidden;background:var(--stage)}
  body{position:relative;font-family:"Montserrat",Arial,sans-serif}

  .card{
    position:absolute;left:346px;width:508px;height:327px;
    border-radius:31px;overflow:hidden;
  }
  .card--front{top:72px}
  .card--back{top:447px}

  .card__backdrop{position:absolute;inset:0}
  .card--front .card__backdrop{
    background:
      radial-gradient(ellipse 70% 75% at 50% 100%, var(--white) 0%, var(--white) 28%, var(--sky-light) 52%, var(--sky-mid) 78%, var(--sky-deep) 100%);
  }
  .card--back .card__backdrop{
    background:
      radial-gradient(ellipse 80% 90% at 50% 70%, var(--lime-bright) 0%, #b4d232 50%, var(--lime-deep) 100%);
  }

  .brand{
    position:absolute;left:0;right:0;top:44px;
    display:flex;flex-direction:column;align-items:center;gap:10px;
  }
  .brand__dot{
    width:74px;height:74px;border-radius:50%;background:var(--navy);
  }
  .brand__name{
    font-weight:800;font-size:44px;line-height:1;letter-spacing:1px;
    color:var(--navy);text-transform:uppercase;
  }
  .brand__tag{
    font-weight:800;font-size:13px;letter-spacing:4px;color:var(--navy);
    text-transform:uppercase;
  }

  .info{
    position:absolute;left:0;right:0;text-align:center;
    font-weight:800;text-transform:uppercase;color:var(--text-blue);
    text-shadow:
      1.5px 0 0 var(--white),-1.5px 0 0 var(--white),
      0 1.5px 0 var(--white),0 -1.5px 0 var(--white),
      1px 1px 0 var(--white),-1px -1px 0 var(--white),
      1px -1px 0 var(--white),-1px 1px 0 var(--white);
  }
  .info__line{display:block;font-size:20px;line-height:24px}
  .info__line--small{font-size:16px;line-height:26px}

  .card--front .info{top:238px}
  .card--back .info{top:206px}
</style>
</head>
<body>

<section class="card card--front">
  <div class="card__backdrop" role="img" aria-label="Sky-blue backdrop with light rays bursting from a bright white glow at the bottom"></div>
  <div class="brand">
    <span class="brand__dot"></span>
    <span class="brand__name">Glintvale</span>
    <span class="brand__tag">Window Cleaning</span>
  </div>
  <div class="info">
    <span class="info__line">612-437-9158 Call or Text</span>
    <span class="info__line">www.GlintvaleCo.com</span>
  </div>
</section>

<section class="card card--back">
  <div class="card__backdrop" role="img" aria-label="Lime green sunburst backdrop with radiating stripes"></div>
  <div class="brand">
    <span class="brand__dot"></span>
    <span class="brand__name">Glintvale</span>
    <span class="brand__tag">Window Cleaning</span>
  </div>
  <div class="info">
    <span class="info__line">Window Cleaning</span>
    <span class="info__line">Gutter Cleaning &amp; Covers</span>
    <span class="info__line">Christmas Lighting</span>
    <span class="info__line info__line--small">200+ 5 Star Reviews</span>
  </div>
</section>

</body>
</html>
```